Lorabelle Hair Flyer - tri-fold

I have added 2 participation payments to the project. I am not sure how I allocate them, but I would like to award them to two particular designers. When I find out how to do it I will allocate them. Thank you to everyone that participated, most designs were outstanding, and it was very hard to chose a winner.
========================================
PLEASE NO NEW DESIGNERS. I HAVE ENOUGH GOOD DESIGNS NOW, THAT I WILL WORK WITH ON THE EXISTING DESIGNERS. THANK YOU FOR ALL PARTICIPATING. THE QUALITY OF ALL SUBMISSIONS HAS EXCEEDED MY EXPECTATIONS, AND IS MAKING THE CHOICE DIFFICULT.
==============================================================

I have attached a proof pdf which is my draft design (I just used a stock template from Printorra) to do the mock up.

I would like you to replace the 3 main pictures of models with those I have attached. The name of the files will tell you where they should go.
I have attached pictures of all the stock photos as well, and most of the text is in the text file to save you typing it in.

I want the background colour to match Lorabelle colours so black with a fade to gold or something like that, must look sophisticated. I have attached Lorabelle logo files in black and white background.

The main pictures I have attached from the models will need to be blended into the background as well, but the hair still needs to be visible (might be hard given it is black hair as well,). The title stripes should be a gold fade as well, and the lorabelle text should be replaced with our logo.

please also add in the Friendsbook and WhatsApp logo's in the appropriate places. The dimensions should be 279mm * 216mm and print in the PrintOrra tri-fold brochure.

Possible ongoing work for the winning person, as the original designer of the logo only does logos/business cards, not other print material. Have logos in other formats (ai/cdr/jpeg) if required

Target Market(s)

African women

Industry/Entity Type

Hair

Font styles to use
Serif

Requirements
Must have
• Logo, product pictures, attached text, layout changes to draft mock up is ok if it looks better. Must conform to Printorra tri-fold layout
Nice to have
• Based on logo colours, black, white, gold complimentary colours to that palette are ok

```html
<!DOCTYPE html>
<html lang="en">
<head>
<meta charset="utf-8">
<title>Lorabelle Hair – Tri-fold Brochure</title>
<link rel="stylesheet" href="https://fonts.googleapis.com/css2?family=Cinzel:wght@400;700&family=Lato:wght@400;700&display=swap">
<style>
  :root{
    --black:#0b0b0b;
    --white:#ffffff;
    --gold:#c39a22;
    --gold-light:#e0bb45;
    --gold-dark:#7a5c10;
    --stage:#d6d6d6;
    --photo-dark:#1a1616;
    --photo-mid:#6b5850;
  }
  *{box-sizing:border-box;margin:0;padding:0}
  html,body{width:1200px;height:844px;overflow:hidden}
  body{background:var(--stage);position:relative;font-family:'Lato',sans-serif}
  .brochure{position:absolute;left:83px;top:22px;width:1034px;height:800px;display:flex;box-shadow:0 6px 18px rgba(0,0,0,.25)}
  .panel{position:relative;width:345px;height:800px;overflow:hidden}
  .panel svg.bg{position:absolute;inset:0}
  .photo-ring{position:absolute;border-radius:50%;border:4px solid var(--gold);background:var(--white);padding:5px}
  .photo{width:100%;height:100%;border-radius:50%;background:radial-gradient(circle at 50% 45%,var(--photo-mid) 0%,var(--photo-dark) 55%,#050505 100%)}

  /* Panel 1 – testimonials */
  .testimonials-title{position:absolute;top:44px;left:0;width:100%;text-align:center;font-family:'Cinzel',serif;color:var(--white);font-size:33px;line-height:40px}
  .quote{position:absolute;left:18px;width:300px}
  .quote-mark{position:absolute;font-family:'Cinzel',serif;font-weight:700;font-size:62px;line-height:1;color:var(--black)}
  .quote-text{margin-left:40px;font-size:12.5px;line-height:16px;color:var(--white);text-align:justify}
  .quote-author{margin-top:22px;text-align:right;font-size:13px;font-weight:700;color:var(--black)}

  /* Logo lockup */
  .logo{position:absolute;text-align:center}
  .logo-dot{display:block;margin:0 auto 10px;width:30px;height:30px;border-radius:50%;background:var(--gold)}
  .logo-name{font-family:'Cinzel',serif;color:var(--white);font-size:32px;letter-spacing:1px;line-height:34px}
  .logo-tag{font-size:12px;color:#9a9a9a;letter-spacing:.5px}

  /* Panel 2 – contact */
  .cta{position:absolute;top:156px;left:0;width:100%;text-align:center}
  .cta-head{font-family:'Cinzel',serif;color:var(--gold);font-size:26px;line-height:30px}
  .cta-sub{font-family:'Cinzel',serif;color:var(--gold);font-size:16px;line-height:18px}
  .cta-line{color:var(--white);font-weight:700;font-size:15.5px;line-height:22px}
  .cta-support{color:var(--white);font-size:19px;line-height:26px}
  .managers{position:absolute;top:425px;left:0;width:100%;text-align:center}
  .manager-role{font-family:'Cinzel',serif;color:var(--gold);font-size:12px;letter-spacing:1px;line-height:16px}
  .manager-name{color:var(--white);font-size:16px;line-height:22px}
  .contact{position:absolute;top:688px;left:0;width:266px;text-align:center;color:var(--black)}
  .contact-head{font-weight:700;font-size:15px}
  .icon-circle{display:block;margin:6px auto 6px;width:24px;height:24px;border-radius:50%;border:2px solid var(--gold)}
  .follow{font-weight:700;font-size:12.5px}
  .handle{display:flex;align-items:center;justify-content:center;gap:4px;font-size:12.5px;color:var(--gold-dark);margin-top:4px}
  .icon-square{width:14px;height:14px;background:var(--gold)}

  /* Panel 3 – cover */
  .cover-title{position:absolute;right:0;top:596px;width:345px;text-align:right;font-family:'Cinzel',serif;line-height:1}
  .cover-brand{color:var(--gold);font-weight:700;font-size:40px}
  .cover-hair{color:var(--black);font-weight:700;font-size:44px;margin-top:2px}
  .cover-tag{position:absolute;left:44px;top:690px;font-size:32px;color:var(--black);white-space:nowrap}
  .url-pill{position:absolute;left:22px;top:737px;width:300px;height:28px;border-radius:14px;background:linear-gradient(90deg,var(--gold-dark),var(--gold) 40%,var(--gold));color:var(--white);font-size:13px;letter-spacing:2.2px;font-weight:700;display:flex;align-items:center;justify-content:center}
</style>
</head>
<body>
<main class="brochure">

  <!-- Inside flap: testimonials -->
  <section class="panel panel-testimonials">
    <svg class="bg" width="345" height="800" viewBox="0 0 345 800" aria-hidden="true">
      <defs>
        <linearGradient id="goldFade" x1="0" x2="1" y1="0" y2="0">
          <stop offset="0" stop-color="#7a5c10"/>
          <stop offset=".5" stop-color="#b38a1e"/>
          <stop offset="1" stop-color="#d4ad3a"/>
        </linearGradient>
      </defs>
      <rect width="345" height="800" fill="url(#goldFade)"/>
      <path d="M0 665 C120 672 240 660 345 610 L345 800 L0 800 Z" fill="#0b0b0b"/>
      <path d="M0 658 C120 664 240 652 345 600" stroke="#e0bb45" stroke-width="5" fill="none"/>
    </svg>
    <h2 class="testimonials-title">Customer<br>Testimonials</h2>
    <div class="quote" style="top:150px">
      <span class="quote-mark" style="left:0;top:-4px">“</span>
      <p class="quote-text">I went to buy 20in straight but ended up buying 22in*2, 16in n 14in ..... I still didn't leave without picking 12in n 14in of the lovely curly beauty</p>
      <span class="quote-mark" style="left:118px;top:52px">”</span>
      <p class="quote-author">Adaeze Okafor (Abuja)</p>
    </div>
    <div class="quote" style="top:300px">
      <span class="quote-mark" style="left:0;top:-4px">“</span>
      <p class="quote-text">Just thought I'd let you know. I used your hair today and it is the best hair I have ever used. Could I get 3 pieces of the 18in Curly for my daughters Wedding</p>
      <span class="quote-mark" style="left:155px;top:52px">”</span>
      <p class="quote-author">Rosalind (Hurstville, Australia)</p>
    </div>
    <div class="photo-ring" style="left:36px;top:482px;width:276px;height:276px">
      <div class="photo" role="img" aria-label="Portrait of a model with long, voluminous black curly hair"></div>
    </div>
  </section>

  <!-- Back panel: contact -->
  <section class="panel panel-contact">
    <svg class="bg" width="345" height="800" viewBox="0 0 345 800" aria-hidden="true">
      <rect width="345" height="800" fill="#ffffff"/>
      <path d="M0 0 H345 V520 C250 560 110 590 0 612 Z" fill="#0b0b0b"/>
      <path d="M0 612 C110 590 250 560 345 520" stroke="#c39a22" stroke-width="8" fill="none"/>
      <path d="M345 560 C300 610 285 700 300 800" stroke="#c39a22" stroke-width="10" fill="none"/>
      <path d="M345 610 C318 660 312 730 322 800" stroke="#e0bb45" stroke-width="5" fill="none"/>
    </svg>
    <div class="cta">
      <p class="cta-head">CALL US TODAY!</p>
      <p class="cta-sub">IF YOU ARE INTERESTED</p>
      <p class="cta-line">in becoming a Lorabelle Hair stockist</p>
      <p class="cta-support">Ask about our marketing support</p>
    </div>
    <div class="logo" style="left:0;top:306px;width:345px">
      <span class="logo-dot"></span>
      <p class="logo-name">LORABELLE</p>
      <p class="logo-tag">100% Human Hair</p>
    </div>
    <div class="managers">
      <p class="manager-role">MANAGER, NIGERIA :</p>
      <p class="manager-name">Chioma &nbsp;0700 555 0182</p>
      <p class="manager-role">AFRICAN SALES MANAGER :</p>
      <p class="manager-name">Marguerite + 61 400 555 017</p>
    </div>
    <div class="contact">
      <p class="contact-head">Contact either on</p>
      <span class="icon-circle"></span>
      <p class="follow">Follow us on Friendsbook</p>
      <p class="handle"><span class="icon-square"></span>Lorabellehairng</p>
    </div>
  </section>

  <!-- Front cover -->
  <section class="panel panel-cover">
    <svg class="bg" width="345" height="800" viewBox="0 0 345 800" aria-hidden="true">
      <rect width="345" height="800" fill="#ffffff"/>
      <path d="M0 0 H215 C320 110 325 320 205 440 C140 500 60 540 0 565 Z" fill="#0b0b0b"/>
      <path d="M215 0 C320 110 325 320 205 440 C140 500 60 540 0 565" stroke="#c39a22" stroke-width="9" fill="none"/>
      <path d="M238 0 C345 120 345 330 222 455 C160 515 70 560 0 590" stroke="#e0bb45" stroke-width="4" fill="none"/>
      <path d="M0 600 C40 580 70 570 95 565 C40 620 20 700 18 800 H0 Z" fill="#c39a22"/>
    </svg>
    <div class="logo" style="left:14px;top:88px;width:225px">
      <span class="logo-dot"></span>
      <p class="logo-name">LORABELLE</p>
      <p class="logo-tag">100% Human Hair</p>
    </div>
    <div class="photo-ring" style="left:14px;top:244px;width:296px;height:296px">
      <div class="photo" role="img" aria-label="Cover portrait of a model with long, voluminous black curly hair"></div>
    </div>
    <div class="cover-title" style="right:10px">
      <p class="cover-brand">LORABELLE</p>
      <p class="cover-hair">HAIR</p>
    </div>
    <p class="cover-tag">100% human hair</p>
    <p class="url-pill">lorabellehair.shopnest.com</p>
  </section>

</main>
</body>
</html>
```